Ladies Clothing Boutique

I would like a lady dressed in a hot sexy dress holding a designer
Handbag with jewelry like a Nacklace and ring on.
I want people to look at this card and say I need to see what's in her store. My store is located In Bermuda which is mostly hot and we carry Clothing, Handbags, Shoes, Jewelry and accessories
Updates

Good Day All, I would like to thank you all for your designs. Some were Fun and colorful but one caught my eye. I will let you know my decision soon. Nella

Target Market(s)

Ladies 18 years to 50

Industry/Entity Type

Jewelry

Contact Information for Business Card

Nella's Wardrobe
Owner/ Buyer: Nella Brisk
Forty Six Marlow Court
Vellum Street, Hamilton KP42
Bermuda
Tel: 441-728-3904 Email: nb03904@quillmail.example

Requirements
Must have
• Must have designer store look. The first 2 uploaded files are how my cards look now which I don't like and the third file is close to how I would like it to look.

```html
<!DOCTYPE html>
<html lang="en">
<head>
<meta charset="utf-8">
<title>Nella's Wardrobe — Business Card</title>
<link rel="stylesheet" href="https://fonts.googleapis.com/css2?family=Cormorant+Garamond:ital,wght@1,600&family=EB+Garamond:wght@500&family=Open+Sans:wght@400&display=swap">
<style>
  :root {
    --page-bg: #efeaec;
    --card-pink: #e7b3dc;
    --card-pink-light: #f6dcef;
    --card-pink-deep: #c97fbe;
    --title-purple: #6a2a78;
    --ink: #2a1f2a;
    --email-white: #fbeefa;
    --swoosh: rgba(255, 255, 255, 0.45);
    --art-a: #f2c2e4;
    --art-b: #d78fc6;
    --art-c: #6ea3d6;
  }
  * { box-sizing: border-box; margin: 0; padding: 0; }
  html, body {
    width: 1200px; height: 900px; overflow: hidden;
    background: var(--page-bg);
  }
  .canvas {
    width: 1200px; height: 900px;
    display: flex; align-items: center; justify-content: center;
  }
  .business-card {
    position: relative;
    width: 1000px; height: 572px;
    border-radius: 14px;
    overflow: hidden;
    background: radial-gradient(ellipse at 30% 20%, var(--card-pink-light) 0%, var(--card-pink) 55%, var(--card-pink-deep) 100%);
    box-shadow: 0 10px 30px rgba(80, 40, 70, 0.25);
  }
  .card-swooshes {
    position: absolute; inset: 0; width: 100%; height: 100%;
    z-index: 0;
  }
  .boutique-art {
    position: absolute; right: 20px; bottom: 0;
    width: 390px; height: 330px;
    border-radius: 50% 40% 0 0 / 40% 40% 0 0;
    background: linear-gradient(160deg, var(--art-a) 0%, var(--art-b) 60%, var(--art-c) 100%);
    opacity: 0.9;
    z-index: 1;
  }
  .brand-block {
    position: absolute; left: 330px; top: 48px;
    z-index: 2;
  }
  .brand-name {
    font-family: "Cormorant Garamond", serif;
    font-style: italic; font-weight: 600;
    font-size: 76px; line-height: 1;
    color: var(--title-purple);
    letter-spacing: 1px;
  }
  .brand-role {
    font-family: "Open Sans", sans-serif;
    font-size: 34px; color: var(--ink);
    text-align: right; margin-top: 2px; padding-right: 20px;
  }
  .contact-block {
    position: absolute; left: 70px; top: 230px;
    font-family: "EB Garamond", serif;
    font-style: normal;
    font-weight: 500; font-size: 29px; line-height: 1.35;
    color: var(--ink);
    z-index: 2;
  }
  .contact-email { color: var(--email-white); }
</style>
</head>
<body>
<main class="canvas">
  <article class="business-card">
    <svg class="card-swooshes" viewBox="0 0 1000 572" aria-hidden="true">
      <path d="M0 140 C 250 60, 520 40, 1000 120" fill="none" stroke="var(--swoosh)" stroke-width="26"/>
      <path d="M-40 470 C 120 300, 420 260, 700 380" fill="none" stroke="var(--swoosh)" stroke-width="18"/>
      <path d="M60 572 C 200 420, 420 400, 620 460" fill="none" stroke="rgba(255,255,255,0.25)" stroke-width="40"/>
      <ellipse cx="240" cy="430" rx="200" ry="90" fill="rgba(255,255,255,0.12)"/>
    </svg>

    <div class="boutique-art" role="img" aria-label="Illustration of two fashionable women carrying shopping bags"></div>

    <header class="brand-block">
      <h1 class="brand-name">Nella's Wardrobe</h1>
      <p class="brand-role">Owner/Buyer</p>
    </header>

    <address class="contact-block">
      <p>Nella Brisk Forty Six Marlow</p>
      <p>Court Vellum Street, Hamilton KP42</p>
      <p>Bermuda Tel: 441-728-3904</p>
      <p class="contact-email">Email: nb03904@quillmail.example</p>
    </address>
  </article>
</main>
</body>
</html>
```